Local Horticulturalist needs Business card design

Meridel Horticulture would like to update our existing business card and utilize our new logo (design attached)....we specialize in getting the best out of our customers yard with professional maintenance programs, expert pruning and hedging and garden restorations.
Utilizing colors from attached logo I would like a design that implies professionalism and if possible our businesses love of restoration through plants.
I also sometimes write down for my customers a start date and price on the back of my current card
Target Market(s)
Home owners
Contractors
Industry/Entity Type
Gardener
Contact Information for Business Card
Gareth Volkstrom | Horticulturalist
ph: 0438275946
meridelhort@fernmail.example
www.meridelhorticulture.example.au
Requirements
Must have
- crucial information easy to read
- incorporate current logo
- Horticulturalist listed preferably near name
Nice to have
- currently I write a job start date and price on the back of my current card so something that integrates this would be beneficial
Should not have
- be pretty or flowerey
- be too white or basic

```html
<!DOCTYPE html>
<html lang="en">
<head>
<meta charset="utf-8">
<title>Meridel Horticulture – Business Card</title>
<link rel="stylesheet" href="https://fonts.googleapis.com/css2?family=Lato:wght@400;700&display=swap">
<style>
  :root {
    --leaf-green: #8cc63f;
    --deep-green: #6fae2e;
    --soil-brown: #7a6a55;
    --ink: #1c1c1c;
    --paper: #ffffff;
    --backdrop: #ecebe8;
  }
  * { margin: 0; padding: 0; box-sizing: border-box; }
  html, body {
    width: 1200px; height: 905px; overflow: hidden;
    background: var(--backdrop);
    font-family: "Lato", Arial, sans-serif;
  }
  .card {
    position: absolute;
    left: 240px;
    width: 720px; height: 412px;
    overflow: hidden;
    box-shadow: 0 4px 14px rgba(0,0,0,.18);
  }
  /* Front */
  .card--front { top: 30px; background: var(--paper); }
  .front-brand {
    position: absolute; left: 120px; top: 160px;
    display: flex; align-items: center; gap: 16px;
  }
  .brand-dot {
    width: 64px; height: 64px; border-radius: 50%;
    background: var(--leaf-green);
  }
  .brand-name {
    font-weight: 700; font-size: 44px; color: var(--leaf-green);
    letter-spacing: .3px;
  }
  .dotted-rule {
    position: absolute; left: 0; right: 0; top: 340px;
    border-top: 3px dotted var(--deep-green);
  }
  /* Back */
  .card--back {
    top: 463px;
    background: linear-gradient(172deg, var(--leaf-green) 0%, #86b845 25%, var(--soil-brown) 85%);
  }
  .back-arc {
    position: absolute; left: 395px; top: -150px;
    width: 470px; height: 470px; border-radius: 50%;
    background: var(--paper);
  }
  .back-mark {
    position: absolute; left: 470px; top: 40px;
    width: 230px; height: 230px; border-radius: 50%;
    background: linear-gradient(160deg, var(--leaf-green) 0%, var(--soil-brown) 70%);
  }
  .back-brand {
    position: absolute; left: 60px; top: 118px;
    display: flex; align-items: center; gap: 10px;
  }
  .back-brand .brand-name { font-size: 26px; color: #6d5f4c; }
  .holder {
    position: absolute; left: 60px; top: 178px;
  }
  .holder-name {
    font-weight: 700; font-size: 26px; color: var(--leaf-green);
  }
  .holder-title {
    font-size: 22px; color: var(--ink); margin-top: 2px;
  }
  .contacts {
    position: absolute; left: 60px; top: 282px;
    list-style: none; font-size: 21px; color: var(--ink);
  }
  .contacts li { display: flex; align-items: center; gap: 8px; line-height: 27px; }
  .contacts svg { width: 18px; height: 18px; flex: none; }
</style>
</head>
<body>

<section class="card card--front" aria-label="Business card front">
  <div class="front-brand">
    <span class="brand-dot" aria-hidden="true"></span>
    <span class="brand-name">Meridel Horticulture</span>
  </div>
  <div class="dotted-rule"></div>
</section>

<section class="card card--back" aria-label="Business card back">
  <div class="back-arc"></div>
  <div class="back-mark" role="img" aria-label="Brand emblem area"></div>

  <div class="back-brand">
    <span class="brand-name">Meridel Horticulture</span>
  </div>

  <div class="holder">
    <p class="holder-name">Gareth Volkstrom</p>
    <p class="holder-title">Horticulturalist</p>
  </div>

  <ul class="contacts">
    <li>
      <svg viewBox="0 0 20 20" aria-hidden="true"><path fill="#d8d2c6" d="M3 7c0-2 3-4 7-4s7 2 7 4v2h-4V7.5H7V9H3zM5 10h10l2 7H3z"/><circle cx="10" cy="13.5" r="2" fill="#7a6a55"/></svg>
      <span>0438275946</span>
    </li>
    <li>
      <svg viewBox="0 0 20 20" aria-hidden="true"><rect x="2" y="4" width="16" height="12" fill="#d8d2c6"/><path d="M2 4l8 7 8-7" fill="none" stroke="#7a6a55" stroke-width="1.5"/></svg>
      <span>meridelhort@fernmail.example</span>
    </li>
    <li>
      <svg viewBox="0 0 20 20" aria-hidden="true"><circle cx="10" cy="10" r="8" fill="#9fcc5a"/><g fill="none" stroke="#fff" stroke-width="1.2"><ellipse cx="10" cy="10" rx="3.5" ry="8"/><path d="M2 10h16M3.5 6h13M3.5 14h13"/></g></svg>
      <span>www.meridelhorticulture.example.au</span>
    </li>
  </ul>
</section>

</body>
</html>
```